30th Anniversary Poster

Need a 2ft (Wide) X 3ft (Tall) Poster design for a 30th anniversary party that will be used in .  Need the get the logo to be the theme colors (gold).  Overall theme is elegance with gold and black being the main colors.  The background should be black.  Silver can be used as an accent color.  I need the sign to say Welcome and 30th Anniversary.  I need all text to be editable and fonts easily available.
A feel similar to images in this search is pretty close.
https://www.travinqo.example/find?sess=b7d2e90c41fa3318&ref=8K4QWTRB_plXM204XM204&tok=QPLMZNXdr4HwYbcEeRt2Uv:1650321478903&q=gala+event+poster&mode=4&flt=ZRPWk7Tt9pLmr41nQa8VcyXeHd2sBjKuvFgNoLQmRzT5Wp8xHcYbDe3KaNfVgUiJoPq7LrSt6MwXz2BvNcQhYdGeKjLmPoRsTuVwXyZaBcDeFgHiJkLmNoPqRsTuVwXyZaBcDeFgHiJkLmNoPqRsTuVw-3AbCdEfGhIj_KlMnOpQrStUvWxYzAbCdEfGhIjKlMnOpQrStUv-WxYzAbCdEfGhIj_KlMnOp&sb=Q&sk=4&vx=3bLPqRtw8Zn2KXwPmLrHnQsTUvWxYzAbCdEfGhIjKl&vw=1440&vh=900&px=2

```html
<!DOCTYPE html>
<html lang="en">
<head>
<meta charset="utf-8">
<title>Welcome – 30th Anniversary</title>
<link rel="stylesheet" href="https://fonts.googleapis.com/css2?family=Montserrat:wght@600;800&family=Oswald:wght@500&display=swap">
<style>
  :root {
    --backdrop: #e9e6e1;
    --poster-black: #0b0a09;
    --poster-deep: #1a1814;
    --gold-light: #f6dc8c;
    --gold: #d4a93f;
    --gold-dark: #8a6420;
    --silver: #c9cbcf;
  }
  html, body {
    margin: 0;
    width: 1094px;
    height: 1200px;
    overflow: hidden;
    background: var(--backdrop);
  }
  .poster {
    position: absolute;
    left: 173px;
    top: 40px;
    width: 747px;
    height: 1120px;
    box-shadow: 0 10px 30px rgba(0,0,0,0.25);
  }
  .brand-name {
    font-family: "Montserrat", sans-serif;
    font-weight: 600;
    font-size: 22px;
    letter-spacing: 2px;
    fill: var(--silver);
  }
  .welcome {
    font-family: "Montserrat", sans-serif;
    font-weight: 800;
    font-size: 66px;
    letter-spacing: 6px;
    fill: url(#goldText);
  }
  .big-number {
    font-family: "Montserrat", sans-serif;
    font-weight: 800;
    font-size: 260px;
    letter-spacing: -8px;
    fill: url(#goldText);
  }
  .ordinal {
    font-family: "Montserrat", sans-serif;
    font-weight: 600;
    font-size: 24px;
    fill: var(--gold);
  }
  .anniversary {
    font-family: "Oswald", sans-serif;
    font-weight: 500;
    font-size: 48px;
    letter-spacing: 7px;
    fill: url(#goldText);
  }
</style>
</head>
<body>
<svg class="poster" viewBox="0 0 747 1120" xmlns="http://www.w3.org/2000/svg">
  <defs>
    <radialGradient id="posterBg" cx="50%" cy="45%" r="70%">
      <stop offset="0" stop-color="var(--poster-deep)"/>
      <stop offset="1" stop-color="var(--poster-black)"/>
    </radialGradient>
    <linearGradient id="goldText" x1="0" y1="0" x2="0" y2="1">
      <stop offset="0" stop-color="var(--gold-light)"/>
      <stop offset="0.55" stop-color="var(--gold)"/>
      <stop offset="1" stop-color="var(--gold-dark)"/>
    </linearGradient>
    <radialGradient id="softGold" cx="50%" cy="50%" r="50%">
      <stop offset="0" stop-color="var(--gold)" stop-opacity="0.22"/>
      <stop offset="1" stop-color="var(--gold)" stop-opacity="0"/>
    </radialGradient>
    <radialGradient id="emblemGlow" cx="50%" cy="50%" r="50%">
      <stop offset="0" stop-color="var(--gold-dark)" stop-opacity="0.28"/>
      <stop offset="0.75" stop-color="var(--gold-dark)" stop-opacity="0.12"/>
      <stop offset="1" stop-color="var(--gold-dark)" stop-opacity="0"/>
    </radialGradient>
    <path id="welcomeArc" d="M 113 510 A 290 290 0 0 1 633 510"/>
  </defs>

  <rect class="poster-bg" width="747" height="1120" fill="url(#posterBg)"/>

  <g class="ribbons" role="img" aria-label="Curling gold ribbons at the top corners">
    <ellipse cx="110" cy="90" rx="140" ry="120" fill="url(#softGold)"/>
    <ellipse cx="640" cy="70" rx="140" ry="120" fill="url(#softGold)"/>
  </g>

  <g class="sparkle-field" role="img" aria-label="Scattered gold sparkles">
    <ellipse cx="373" cy="1000" rx="330" ry="110" fill="url(#softGold)"/>
  </g>

  <g class="brand">
    <circle cx="240" cy="137" r="10" fill="var(--gold)"/>
    <text class="brand-name" x="260" y="145">HARLOW SYSTEMS</text>
  </g>

  <text class="welcome" text-anchor="middle">
    <textPath href="#welcomeArc" startOffset="50%">WELCOME</textPath>
  </text>

  <ellipse class="emblem" role="img" aria-label="Gold anniversary emblem with arc, three stars and ribbon banner" cx="373" cy="640" rx="290" ry="250" fill="url(#emblemGlow)"/>

  <text class="big-number" x="365" y="712" text-anchor="middle">30</text>
  <text class="ordinal" x="540" y="540">TH</text>

  <text class="anniversary" x="373" y="822" text-anchor="middle">ANNIVERSARY</text>
</svg>
</body>
</html>
```